Australian Meat, Seafood and Fresh Produce Website

Our organization is looking to design a simple, but eye catching website to show our services.
Our company exports West Australian FRESH fruit and vegetables, seafood and meat.
The website we are looking for would consist of:
- Landing Page
- Company info
- Directors bio
- Page that highlights our products
- Contact us page
We would like it to have a Chinese translated version as well.
Milo
Target Market(s)
Chinese Market
Industry/Entity Type
It Company
Number of Pages Required
1 page
Look and feel
Each slider illustrates characteristics of the customer's brand and the style your logo design should communicate.

```html
<!DOCTYPE html>
<html lang="en">
<head>
<meta charset="utf-8">
<title>Coastline Fresh Exports</title>
<link rel="stylesheet" href="https://fonts.googleapis.com/css2?family=Arimo:wght@400;700&family=Pacifico&display=swap">
<style>
:root{
  --green-dark:#2f5b05;
  --green-mid:#4d8a0c;
  --green-light:#8cc63f;
  --lime:#a9cf2e;
  --hello:#b6cf17;
  --ink:#1f3b02;
  --text:#2b3a12;
  --white:#ffffff;
  --search:#eef5c2;
  --go:#2a4a06;
  --tile-red:#e2401c;
  --tile-green:#5a9a16;
  --tile-orange:#ec6a1e;
  --tile-amber:#f29a12;
  --card:#2e2e2e;
  --panel-border:#c9c9c9;
  --footer:#7b7b7b;
  --footer-text:#f2f2f2;
}
*{margin:0;padding:0;box-sizing:border-box}
html,body{width:1200px;height:2921px;overflow:hidden}
body{font-family:"Arimo",Arial,sans-serif;background:#fbfbf8;position:relative;color:var(--text)}
.abs{position:absolute}

/* header */
.site-header{left:0;top:0;width:1200px;height:280px;background:linear-gradient(#5f9a0f 0%,#3f7608 45%,#2c5a04 70%,#3e7a07 100%)}
.brand{left:68px;top:58px;font-size:40px;font-weight:700;color:var(--white)}
.account-links{right:28px;top:18px;font-size:18px;color:var(--white);text-align:right;line-height:24px}
.search{left:755px;top:131px;width:316px;height:40px;background:var(--search);font-size:19px;letter-spacing:4px;color:#7a8a50;padding:9px 18px}
.search-go{left:1071px;top:131px;width:102px;height:40px;background:var(--go);color:var(--white);font-weight:700;font-size:24px;text-align:center;line-height:40px}
.main-nav{left:0;top:187px;width:1200px;height:93px;background:linear-gradient(#66a314,#3f7a08);display:flex;justify-content:center;align-items:center;gap:26px;font-size:30px;color:var(--white)}
.main-nav .sep{opacity:.9}

/* hero */
.hero{left:0;top:280px;width:1200px;height:590px;background:radial-gradient(circle at 30% 40%,#e84a2a 0%,transparent 35%),radial-gradient(circle at 65% 35%,#4a2f5a 0%,transparent 30%),radial-gradient(circle at 80% 70%,#f0c030 0%,transparent 30%),radial-gradient(circle at 15% 75%,#f7a21a 0%,transparent 30%),linear-gradient(#f6f6f0,#d8e08a)}
.hero-arrow{top:494px;width:48px;height:139px;background:rgba(210,210,210,.85)}
.hero-arrow svg{display:block;margin:42px auto 0}

/* product band */
.band{left:0;top:864px;width:1200px;height:426px;background:linear-gradient(#9fcb2a,#b9dc34 50%,#a3cf2c)}
.zig{left:0;width:1200px;height:14px}
.tile{top:896px;width:212px;height:370px;box-shadow:0 3px 6px rgba(0,0,0,.25)}
.tile-photo{height:241px}
.tile-label{height:129px;color:var(--white);font-size:22px;padding:38px 0 0 40px;line-height:30px}

/* intro */
.hello{left:134px;top:1322px;font-family:"Pacifico",cursive;font-size:72px;color:var(--hello)}
.intro-title{left:409px;top:1354px;width:720px;font-size:31px;font-weight:700;color:var(--ink);line-height:38px}
.intro-copy{left:414px;top:1448px;width:742px;font-size:18px;line-height:23px;color:var(--text);text-align:justify}
.intro-copy p{margin-bottom:23px}

.section-title{left:0;width:1200px;text-align:center;font-size:26px;font-weight:700;color:var(--ink)}
.member{top:1784px;width:210px;text-align:center}
.member-photo{width:146px;height:140px;margin:0 auto;background:var(--card);border-radius:10px;box-shadow:0 2px 4px rgba(0,0,0,.3)}
.member-name{font-size:20px;line-height:22px;margin-top:12px;color:var(--ink)}
.member-role{font-size:12px;line-height:14px;text-align:left;margin-top:5px;color:var(--text)}

/* suppliers */
.supplier-panel{left:146px;top:2060px;width:908px;height:576px;background:var(--white);border:2px solid var(--panel-border);border-radius:8px;box-shadow:0 1px 4px rgba(0,0,0,.15)}
.supplier{top:2078px;width:245px}
.supplier-name{height:64px;display:flex;align-items:center;justify-content:center;font-size:26px;font-weight:700;color:var(--ink);text-align:center;line-height:28px}
.supplier-tag{font-size:15px;text-align:center;margin-top:28px;color:var(--text)}
.supplier-photo{height:122px;margin-top:16px}
.supplier-copy{font-size:13.5px;line-height:22px;margin-top:20px;color:var(--text)}

/* footer */
.site-footer{left:0;top:2697px;width:1200px;height:224px;background:var(--footer)}
.footer-brand{left:68px;top:2724px;font-size:30px;font-weight:700;color:var(--white);white-space:nowrap}
.footer-tag{left:72px;top:2774px;width:340px;font-size:14.5px;font-weight:700;color:var(--white);line-height:19px}
.footer-col{top:2725px;font-size:16px;font-weight:700;color:var(--footer-text);line-height:21px}
.footer-col h4{font-size:16px;margin-bottom:17px}
</style>
</head>
<body>

<header class="abs site-header"></header>
<div class="abs brand">Coastline Fresh Exports</div>
<div class="abs account-links">Sign up (create account) &nbsp;&nbsp;|&nbsp;&nbsp; Log in<br>Call: 0000 9876 543 210</div>
<div class="abs search">SEARCH</div>
<div class="abs search-go">GO</div>
<nav class="abs main-nav">
  <span>HOME</span><span class="sep">|</span><span>ABOUT US</span><span class="sep">|</span><span>PRODUCTS</span><span class="sep">|</span><span>CONTACT US</span>
</nav>

<div class="abs hero" role="img" aria-label="Photograph of a heap of fresh fruit: pineapple, apples, grapes, pomegranate, strawberries, oranges, pears and bananas"></div>
<div class="abs hero-arrow" style="left:15px"><svg width="24" height="56" viewBox="0 0 24 56"><path d="M20 4 L6 28 L20 52" fill="none" stroke="#1f3b02" stroke-width="6"/></svg></div>
<div class="abs hero-arrow" style="left:1137px"><svg width="24" height="56" viewBox="0 0 24 56"><path d="M4 4 L18 28 L4 52" fill="none" stroke="#1f3b02" stroke-width="6"/></svg></div>

<section class="abs band"></section>
<svg class="abs zig" style="top:858px" viewBox="0 0 1200 14" preserveAspectRatio="none">
  <defs><pattern id="zigDown" width="20" height="14" patternUnits="userSpaceOnUse"><polygon points="0,0 20,0 10,14" fill="#fbfbf8"/></pattern></defs>
  <rect width="1200" height="14" fill="#a0cc2a"/><rect width="1200" height="14" fill="url(#zigDown)"/>
</svg>
<svg class="abs zig" style="top:1282px" viewBox="0 0 1200 14" preserveAspectRatio="none">
  <defs><pattern id="zigUp" width="20" height="14" patternUnits="userSpaceOnUse"><polygon points="0,14 20,14 10,0" fill="#fbfbf8"/></pattern></defs>
  <rect width="1200" height="14" fill="#a3cf2c"/><rect width="1200" height="14" fill="url(#zigUp)"/>
</svg>

<div class="abs tile" style="left:173px">
  <div class="tile-photo" role="img" aria-label="Photograph of red apples" style="background:radial-gradient(circle at 50% 60%,#e8452a,#a8200e)"></div>
  <div class="tile-label" style="background:linear-gradient(#e9501f,var(--tile-red))">FRESH<br>Fruits</div>
</div>
<div class="abs tile" style="left:389px">
  <div class="tile-photo" role="img" aria-label="Photograph of green cabbage leaves" style="background:radial-gradient(circle at 50% 50%,#b6d97a,#4f8a22)"></div>
  <div class="tile-label" style="background:linear-gradient(#6fae1c,var(--tile-green))">FRESH<br>Vegetables</div>
</div>
<div class="abs tile" style="left:606px">
  <div class="tile-photo" role="img" aria-label="Photograph of crayfish and seafood on ice" style="background:radial-gradient(circle at 50% 50%,#c9a08a,#6a5a62)"></div>
  <div class="tile-label" style="background:linear-gradient(#f07a28,var(--tile-orange))">FRESH<br>Seafoods</div>
</div>
<div class="abs tile" style="left:823px">
  <div class="tile-photo" role="img" aria-label="Photograph of cuts of red meat" style="background:radial-gradient(circle at 50% 50%,#c84a4a,#7a1f22)"></div>
  <div class="tile-label" style="background:linear-gradient(#f5a824,var(--tile-amber))">HIGH QUALITY<br>Meat</div>
</div>

<div class="abs hello">Hello</div>
<h1 class="abs intro-title">Our company exports West Australian FRESH fruit and vegetables, seafood and meat.</h1>
<div class="abs intro-copy">
  <p>Coastline Fresh Exports (CFE) aims to supply high quality West Australian produce to the rest of the World. Western Australia is known for its high quality farming practices and environment, which produces meat, seafood, fruit and vegetable of a caliber that is respected globally.</p>
  <p>With a management team and first class suppliers allows our organization to provide quality ingredients, straight from farm or ocean to purchaser, in a timely manner to the highest quality.</p>
  <p>This document aims to outline both our management team and their back grounds, as well as the suppliers who will initially be supply our global customers.</p>
</div>

<h2 class="abs section-title" style="top:1731px">Our Management Team</h2>
<div class="abs member" style="left:172px"><div class="member-photo"></div><div class="member-name">Daniel Brooks</div><div class="member-role">Manager of operations, Chinese liaison, Quality processes and management</div></div>
<div class="abs member" style="left:387px"><div class="member-photo"></div><div class="member-name">Owen Tan</div><div class="member-role">Procurement and liaison with suppliers.</div></div>
<div class="abs member" style="left:603px"><div class="member-photo"></div><div class="member-name">Lucas Hart</div><div class="member-role">Logistics, transport, customs and tariffs</div></div>
<div class="abs member" style="left:820px"><div class="member-photo"></div><div class="member-name">Dr. Mei Lin Zhou</div><div class="member-role">Chinese Market Specialist, liaison between Australia and Chinese activities.</div></div>

<h2 class="abs section-title" style="top:2022px">Our Produce Suppliers</h2>
<div class="abs supplier-panel"></div>

<div class="abs supplier" style="left:168px">
  <div class="supplier-name">Prime Pasture Meats</div>
  <div class="supplier-tag">High quality beef, lamb and pork</div>
  <div class="supplier-photo" role="img" aria-label="Photograph of a raw beef cut" style="background:linear-gradient(90deg,#f1f1f1 35%,#c0434a 65%,#e9e9e9)"></div>
  <div class="supplier-copy">Four generations of experience in the beef industry means we are a trusted name in cattle husbandry, feed lotting and grain feed development. Coupled with a commitment to safety, the environment and compliance to quality and Halal requirements, we are a modern, internationally recognised brand that is shaping the next generation of global beef supply. Truly a heritage of fine beef.</div>
</div>
<div class="abs supplier" style="left:484px">
  <div class="supplier-name">Greenrow Growers</div>
  <div class="supplier-tag">Fresh Fruit and Vegetables</div>
  <div class="supplier-photo" role="img" aria-label="Photograph of diced fresh vegetables" style="background:linear-gradient(90deg,#ffffff 35%,#f5a31c 60%,#8cc63f)"></div>
  <div class="supplier-copy">The supplier group operates at all levels of the supply chain from catching, to processing, manufacturing, importing, exporting, wholesaling and retailing. With over 500 employees and a proud history of over 85 years, it is Australia's leading food group, partnering many of Australia's leading corporations in developing solutions that deliver class leading value.</div>
</div>
<div class="abs supplier" style="left:791px">
  <div class="supplier-name">Bluewater Catch</div>
  <div class="supplier-tag">Fresh Seafood</div>
  <div class="supplier-photo" role="img" aria-label="Photograph of a deep blue ocean" style="background:radial-gradient(circle at 50% 30%,#3f73b8,#0b2a63)"></div>
  <div class="supplier-copy">Their innovation has brought new techniques, recipes, and flavor combinations to customers and chefs across Australia. We regularly deliver to quarantine zones, mine sites, large retail outlets, fast food chains, government organisations, aged care facilities, production kitchens and food manufacturers.</div>
</div>

<footer class="abs site-footer"></footer>
<div class="abs footer-brand">Coastline Fresh Exports</div>
<div class="abs footer-tag">aims to supply high quality West Australian produce to the rest of the World.</div>
<div class="abs footer-col" style="left:482px"><h4>ABOUT US</h4>&gt; Contact<br>&gt; Delivery<br>&gt; Terms &amp; Conditions</div>
<div class="abs footer-col" style="left:725px"><h4>OUR OFFERS</h4>&gt; New Products<br>&gt; Top Sellers<br>&gt; Specials</div>
<div class="abs footer-col" style="left:966px"><h4>CATEGORIES</h4>&gt; Fruits &amp; Vegetables<br>&gt; Seafoods<br>&gt; Meat</div>

</body>
</html>
```